Ventrel Advisory Inc. (Enterprise Resource Planning - All KORVA)

I need a logo and business card design for an ERP consulting company based in Dallas, We specifically provide consulting services for implementing and maintaining KORVA ERP systems, I would like to see all the colors be navy and white. White Card on one side with Navy print, and Navy card on the other side with White print. The design should communicate that we "Ventrel" results by effort, skill and courage.

Target Market(s)

Pinnacle 400 companies that are implementing or maintaining an KORVA ERP system. My specialty is Finance and Controlling

Industry/Entity Type

Business Consultant

Contact Information for Business Card

Dana Welby
President / CEO

3820 Brinlow Lane
Marrowfield, Dellmont 40291

Tel: 555-014-0187
eMail: dana.welby@ventreladvisory.example
web: www.ventreladvisory.example

Logo Text

This needs to be a Graphic Design

Font styles to use
Sans Serif

Colors
0555a3
ffffff

Requirements
Must have
• two sided
• Front side - Navy card with white print
• name, title, telephone, email
• Back side - White card with navy print
• street address, web address,
• Slogan [Ventrel ~ Effort, Skill, and Courage}
Nice to have
• Classic and Clean
Should not have
• typical IT stuff... we are a consulting service organization not an IT department.

```html
<!DOCTYPE html>
<html lang="en">
<head>
<meta charset="utf-8">
<title>Ventrel Advisory – Business Card</title>
<link rel="stylesheet" href="https://fonts.googleapis.com/css2?family=Arimo:wght@400;700&family=Marcellus&display=swap">
<style>
  :root {
    --navy: #1f5aa8;
    --navy-deep: #16448a;
    --navy-ink: #1b4f9f;
    --white: #ffffff;
    --frame: #4a4a92;
    --ghost: #e6e4f0;
    --label: #2a2a2a;
    --rule: #9a9a9a;
  }
  * { margin: 0; padding: 0; box-sizing: border-box; }
  html, body {
    width: 1014px; height: 1200px; overflow: hidden;
    background: var(--white);
    font-family: "Arimo", Arial, sans-serif;
  }
  .sheet { position: relative; width: 1014px; height: 1200px; }

  .card { position: absolute; overflow: hidden; }

  .card--front {
    left: 143px; top: 143px; width: 723px; height: 417px;
    box-shadow: 2px 2px 0 #111;
  }
  .card__texture { position: absolute; inset: 0; width: 100%; height: 100%; }

  .card__ghost-name {
    position: absolute; font-weight: 700; white-space: nowrap; line-height: 1;
  }
  .card--front .card__ghost-name {
    left: 20px; top: 110px; font-size: 120px;
    color: var(--navy-deep); opacity: 0.4;
  }

  .front__person, .front__contact {
    position: absolute; right: 19px; text-align: right; color: var(--white);
  }
  .front__person { top: 209px; font-weight: 700; font-size: 20px; line-height: 34px; }
  .front__person .name { padding-right: 7px; }
  .front__contact { top: 332px; font-size: 20px; line-height: 28px; letter-spacing: 0.2px; }

  .card--back {
    left: 141px; top: 668px; width: 723px; height: 413px;
    border: 1px solid var(--frame);
  }
  .card--back .card__ghost-name {
    left: 50%; top: 95px; transform: translateX(-50%);
    font-size: 150px; color: var(--ghost); opacity: 0.8;
  }
  .back__slogan, .back__address, .back__web {
    position: absolute; left: 0; right: 0; text-align: center;
    color: var(--navy-ink); font-weight: 700; font-size: 17.5px;
  }
  .back__slogan { top: 183px; left: -8px; }
  .back__address { top: 282px; line-height: 26px; }
  .back__web { top: 356px; }

  .side-label {
    position: absolute; left: 143px;
    font-family: "Marcellus", "Times New Roman", serif;
    font-size: 21px; letter-spacing: -1px; color: var(--label);
  }
  .side-label--front { top: 582px; }
  .side-label--back { top: 1106px; left: 145px; }
  .side-rule {
    position: absolute; left: 143px; width: 551px; height: 2px;
    background: linear-gradient(90deg, #cfcfcf, var(--rule) 40%, #8a8a8a 60%, #e2e2e2);
  }
  .side-rule--front { top: 613px; }
  .side-rule--back { top: 1138px; left: 145px; }
</style>
</head>
<body>
<main class="sheet">

  <section class="card card--front">
    <svg class="card__texture" role="img" aria-label="Navy woven linen texture background" viewBox="0 0 723 417" preserveAspectRatio="none">
      <defs>
        <linearGradient id="linen" x1="0" y1="0" x2="1" y2="1">
          <stop offset="0" stop-color="#2261b0"/>
          <stop offset="0.5" stop-color="#1f5aa8"/>
          <stop offset="1" stop-color="#1a4f99"/>
        </linearGradient>
      </defs>
      <rect width="723" height="417" fill="url(#linen)"/>
    </svg>
    <div class="card__ghost-name" aria-hidden="true">Ventrel</div>
    <div class="front__person">
      <div class="name">Dana Welby</div>
      <div class="title">President/CEO</div>
    </div>
    <div class="front__contact">
      <div>Tel: 555-014-0187</div>
      <div>dana.welby@ventreladvisory.example</div>
    </div>
  </section>

  <h2 class="side-label side-label--front">FRONT DESIGN</h2>
  <div class="side-rule side-rule--front"></div>

  <section class="card card--back">
    <div class="card__ghost-name" aria-hidden="true">Ventrel</div>
    <p class="back__slogan">Ventrel ~ Effort, Skill, and Courage</p>
    <p class="back__address">3820 Brinlow Lane<br>Marrowfield, Dellmont 40291</p>
    <p class="back__web">www.ventreladvisory.example</p>
  </section>

  <h2 class="side-label side-label--back">BACK DESIGN</h2>
  <div class="side-rule side-rule--back"></div>

</main>
</body>
</html>
```